Website Design for Employee Moral and Happiness Company

Looking for a clean website design that explains our features in a step by step manner so our visitors know exactly what our site does before logging in.

The site is called "Velquo". See logo design and video for a sample of style and an overview of what we do.

Target Market(s)

Business owners that are looking to retain employees.

Number of Pages Required

1 page

```html
<!DOCTYPE html>
<html lang="en">
<head>
<meta charset="utf-8">
<title>Velquo – Employee Morale &amp; Happiness</title>
<link rel="stylesheet" href="https://fonts.googleapis.com/css2?family=Poppins:wght@400;500;600;700;800&display=swap">
<style>
:root{
  --orange:#f26a10;
  --orange-soft:#fde3d2;
  --ink:#111111;
  --text:#333333;
  --muted:#555555;
  --white:#ffffff;
  --dark:#1b1b1b;
  --peach:#f7e7dc;
}
*{margin:0;padding:0;box-sizing:border-box}
html,body{width:1200px;height:4241px;overflow:hidden;background:var(--white)}
body{font-family:"Poppins",sans-serif;color:var(--text)}
.page{position:relative;width:1200px;height:4241px;overflow:hidden}
.abs{position:absolute}
.btn{position:absolute;display:flex;align-items:center;justify-content:center;border-radius:30px;background:var(--orange);color:var(--white);font-weight:700;font-size:15px;letter-spacing:.3px;text-transform:uppercase}
.h2{position:absolute;font-weight:800;font-size:44px;line-height:1.2;color:var(--ink);letter-spacing:.5px}
.para{position:absolute;font-size:18.5px;line-height:34px;color:var(--text)}

/* header */
.topbar{left:680px;top:0;width:520px;height:40px;background:var(--orange);border-bottom-left-radius:22px;color:var(--white);font-size:15px;display:flex;align-items:center;gap:22px;padding-left:54px}
.topbar svg{vertical-align:-3px;margin-right:8px}
.logo{left:79px;top:28px;font-size:40px;font-weight:700;color:var(--ink);letter-spacing:.5px}
.nav{left:428px;top:66px;display:flex;gap:27px;font-size:15px;font-weight:500;color:#444}
.nav .active{color:var(--orange);position:relative}
.nav .active::after{content:"";position:absolute;left:50%;top:26px;width:22px;height:4px;transform:translateX(-50%);background:radial-gradient(circle,var(--orange) 2px,transparent 2.5px) 0 0/7px 4px repeat-x}
.login{left:934px;top:56px;width:152px;height:42px;border:2px solid #999;border-radius:22px;display:flex;align-items:center;justify-content:center;color:var(--orange);font-size:14px;font-weight:700;gap:6px}

/* hero */
.hero-bg{left:0;top:113px;width:1200px;height:660px}
.slide-tab{top:270px;width:33px;height:72px;background:#777;display:flex;align-items:center;justify-content:center}
.hero-kicker{left:79px;top:214px;font-size:33px;line-height:44px;letter-spacing:1.5px;color:var(--ink);display:flex;align-items:center;gap:14px}
.hero-kicker::after{content:"";width:104px;height:2px;background:var(--ink)}
.hero-title{left:79px;top:262px;font-size:72px;line-height:1;font-weight:800;color:var(--ink);letter-spacing:.5px}
.hero-text{left:79px;top:336px;font-size:20px;line-height:34px;color:var(--ink)}

/* features */
.feature-title{position:absolute;color:var(--white);font-weight:700;font-size:19px;text-transform:uppercase}
.feature-text{position:absolute;color:var(--white);font-size:18.5px;line-height:34px}
.feature-icon{position:absolute;width:89px;height:89px;border-radius:50%;background:var(--white);display:flex;align-items:center;justify-content:center}

/* form */
.field{position:absolute;background:var(--white);border-radius:4px;font-size:16px;color:#555;padding:14px 18px}

/* footer */
.fhead{position:absolute;top:3928px;font-weight:800;font-size:20px;color:var(--ink)}
.flist{position:absolute;top:3962px;font-size:17px;line-height:34px;color:var(--text);list-style:none}
.social{position:absolute;top:4072px;width:45px;height:45px;border:2px solid var(--orange);border-radius:8px}
.cicon{position:absolute;left:890px;width:46px;height:46px;border-radius:8px;background:var(--orange);display:flex;align-items:center;justify-content:center}
</style>
</head>
<body>
<div class="page">

  <!-- hero background -->
  <svg class="abs hero-bg" viewBox="0 113 1200 660" width="1200" height="660" aria-hidden="true">
    <defs>
      <linearGradient id="heroFade" x1="0" y1="0" x2="1" y2="0">
        <stop offset="0" stop-color="#fbeee5"/>
        <stop offset="1" stop-color="#f3ddcd"/>
      </linearGradient>
    </defs>
    <path d="M0 113H1200V530Q600 800 0 530Z" fill="url(#heroFade)"/>
    <path d="M90 590Q600 830 1110 590Q600 770 90 590Z" fill="var(--orange)"/>
    <circle cx="600" cy="728" r="36" fill="var(--orange)"/>
    <path d="M600 712V742M591 733L600 742L609 733" stroke="#fff" stroke-width="2" fill="none"/>
  </svg>
  <div class="abs" role="img" aria-label="Office interior photograph behind the hero" style="left:0;top:113px;width:1200px;height:420px;background:linear-gradient(90deg,rgba(240,215,198,.25),rgba(230,200,180,.35))"></div>

  <!-- header -->
  <div class="abs topbar">
    <span><svg width="16" height="16" viewBox="0 0 24 24"><path fill="#fff" d="M6.6 10.8a15 15 0 0 0 6.6 6.6l2.2-2.2a1 1 0 0 1 1-.25 11.4 11.4 0 0 0 3.6.57 1 1 0 0 1 1 1V20a1 1 0 0 1-1 1A17 17 0 0 1 3 4a1 1 0 0 1 1-1h3.5a1 1 0 0 1 1 1c0 1.25.2 2.45.57 3.57a1 1 0 0 1-.25 1z"/></svg>555-014-2290</span>
    <span style="opacity:.7">|</span>
    <span><svg width="16" height="16" viewBox="0 0 24 24"><path fill="#fff" d="M3 9l9-6 9 6v11H3z"/><path d="M6 11l6 4 6-4" stroke="var(--orange)" stroke-width="2" fill="none"/></svg>info@velquo.com</span>
  </div>
  <div class="abs logo">Velquo</div>
  <nav class="abs nav">
    <span class="active">HOME</span><span>ABOUT US</span><span>OUR FEATURES</span><span>BLOG</span><span>CONTACT</span>
  </nav>
  <div class="abs login">
    <svg width="16" height="16" viewBox="0 0 24 24" fill="none" stroke="var(--orange)" stroke-width="2"><circle cx="12" cy="8" r="4"/><path d="M4 21c0-4 4-6 8-6s8 2 8 6"/></svg>| LOG IN
  </div>

  <!-- hero -->
  <div class="abs slide-tab" style="left:0"><svg width="12" height="12" viewBox="0 0 12 12"><path d="M8 2L4 6L8 10" stroke="#fff" stroke-width="2" fill="none"/></svg></div>
  <div class="abs slide-tab" style="right:0"><svg width="12" height="12" viewBox="0 0 12 12"><path d="M4 2L8 6L4 10" stroke="#fff" stroke-width="2" fill="none"/></svg></div>
  <div class="abs hero-kicker">To Help Business</div>
  <h1 class="abs hero-title">LIKE YOURS</h1>
  <p class="abs hero-text">Lorem ipsum dolor sit amet consectetuo<br>nun adipis elitsed do eiusmod tempor</p>
  <div class="btn" style="left:80px;top:427px;width:212px;height:52px">Contact Us</div>
  <div class="abs" role="img" aria-label="Large Velquo mascot illustration" style="left:590px;top:185px;width:510px;height:370px;border-radius:48%;background:radial-gradient(circle at 50% 45%,rgba(242,106,16,.35),rgba(242,106,16,.08) 70%,transparent 72%)"></div>

  <!-- about -->
  <div class="abs" role="img" aria-label="Decorative halftone ring around the photo" style="left:78px;top:815px;width:510px;height:490px;border-radius:50%;background:radial-gradient(circle,rgba(242,106,16,.14) 60%,transparent 71%)"></div>
  <div class="abs" role="img" aria-label="Photo of a smiling businessman in an office with a colleague on the phone behind" style="left:123px;top:848px;width:410px;height:410px;border-radius:50%;background:linear-gradient(135deg,#cfd3d6,#8c8f93 60%,#5a5f66);box-shadow:0 10px 30px rgba(0,0,0,.15)"></div>
  <h2 class="h2" style="left:635px;top:892px">ABOUT US</h2>
  <p class="para" style="left:635px;top:957px;width:500px">Lorem ipsum dolor sit amet consectetur adipiscingi elit sed do eiusmod tempor incididunt ut labore eto dolore magna aliqua. Quis ipsum suspendisse des ultrices gravida. Risus commodo viverra maecenas accumsan lacus vel facilisis licius decorat.</p>
  <div class="btn" style="left:635px;top:1157px;width:187px;height:52px">About Us</div>

  <!-- features -->
  <svg class="abs" style="left:0;top:1370px" width="1200" height="840" viewBox="0 1370 1200 840" aria-hidden="true">
    <path d="M0 1530Q600 1220 1200 1530V2060Q600 2330 0 2060Z" fill="var(--orange)"/>
  </svg>
  <div class="abs" role="img" aria-label="Team photograph tinted orange behind the features" style="left:0;top:1372px;width:1200px;height:833px;background:radial-gradient(ellipse at 20% 60%,rgba(120,40,0,.18),transparent 55%),radial-gradient(ellipse at 85% 55%,rgba(120,40,0,.15),transparent 55%);clip-path:ellipse(75% 55% at 50% 50%)"></div>
  <h2 class="h2" style="left:0;width:1200px;top:1430px;text-align:center;color:var(--white)">OUR FEATURE</h2>
  <p class="para" style="left:0;width:1200px;top:1494px;text-align:center;color:var(--white)">Lorem ipsum dolor sit amet consectetur adipiscingi<br>elit sed do eiusmod tempor incididunt ut labore</p>

  <svg class="abs" style="left:398px;top:1618px" width="400" height="400" viewBox="0 0 400 400" aria-hidden="true">
    <circle cx="200" cy="200" r="193" fill="none" stroke="#fff" stroke-width="2"/>
    <circle cx="200" cy="7" r="6" fill="#fff"/><circle cx="200" cy="393" r="6" fill="#fff"/>
    <circle cx="7" cy="200" r="6" fill="#fff"/><circle cx="393" cy="200" r="6" fill="#fff"/>
    <circle cx="200" cy="200" r="168" fill="var(--orange)" stroke="#fff" stroke-width="3"/>
  </svg>
  <div class="abs" role="img" aria-label="Round Velquo mascot emblem" style="left:448px;top:1668px;width:300px;height:300px;border-radius:50%;background:radial-gradient(circle at 50% 35%,#ffffff,#fde3d2 60%,#f6a877);box-shadow:0 0 0 10px #e85f08"></div>

  <div class="feature-icon" style="left:79px;top:1600px"><svg width="50" height="50" viewBox="0 0 50 50" fill="none" stroke="var(--orange)" stroke-width="2"><path d="M4 25Q25 5 46 25Q25 45 4 25Z"/><circle cx="25" cy="25" r="8"/><circle cx="25" cy="25" r="3"/></svg></div>
  <div class="feature-title" style="left:79px;top:1694px">Clear Executive Vision</div>
  <p class="feature-text" style="left:79px;top:1726px">dolore magna aliquat enim ad<br>minim veniam quis nostrud.</p>

  <div class="feature-icon" style="left:79px;top:1822px"><svg width="50" height="50" viewBox="0 0 50 50" fill="none" stroke="var(--orange)" stroke-width="2"><circle cx="15" cy="31" r="10"/><circle cx="35" cy="31" r="10"/><path d="M10 22L14 10H20L22 24M40 22L36 10H30L28 24M22 28H28"/></svg></div>
  <div class="feature-title" style="left:79px;top:1927px">Employee Retention</div>
  <p class="feature-text" style="left:79px;top:1959px">dolore magna aliquat enim ad<br>minim veniam quis nostrud.</p>

  <div class="feature-icon" style="left:828px;top:1600px"><svg width="50" height="50" viewBox="0 0 50 50" fill="none" stroke="var(--orange)" stroke-width="2"><path d="M14 24V12h5v10M19 10h5v12M24 10h5v12M29 12h5v16l-4 8H18l-4-6V24"/><circle cx="33" cy="37" r="7"/><path d="M30 37l2 2 4-4"/></svg></div>
  <div class="feature-title" style="left:828px;top:1694px">Passion &amp; Impact</div>
  <p class="feature-text" style="left:828px;top:1726px">dolore magna aliquat enim ad<br>minim veniam quis nostrud.</p>

  <div class="feature-icon" style="left:828px;top:1822px"><svg width="50" height="50" viewBox="0 0 50 50" fill="none" stroke="var(--orange)" stroke-width="2"><rect x="7" y="11" width="36" height="32" rx="3"/><path d="M7 19H43M16 7V14M34 7V14M25 24l3 6h6l-5 4 2 6-6-4-6 4 2-6-5-4h6z"/></svg></div>
  <div class="feature-title" style="left:828px;top:1927px">Event Planner</div>
  <p class="feature-text" style="left:828px;top:1959px">dolore magna aliquat enim ad<br>minim veniam quis nostrud.</p>

  <div class="btn" style="left:459px;top:2066px;width:282px;height:52px;background:var(--ink)">View More Features</div>

  <!-- promise -->
  <h2 class="h2" style="left:80px;top:2333px">WHAT WE PROMISE</h2>
  <p class="para" style="left:80px;top:2397px;width:480px">Lorem ipsum dolor sit amet consectetur adipiscingi elit sed do eiusmod tempor incididunt ut labore eto dolore magna aliqua. Quis ipsum suspendisse des ultrices gravida. Risus commodo viverra maecenas accumsan lacus vel facilisis licius decorat.</p>
  <div class="btn" style="left:80px;top:2597px;width:212px;height:52px">Contact Us</div>
  <div class="abs" aria-hidden="true" style="left:620px;top:2340px;width:482px;height:348px;background:var(--orange);border-radius:60px 0 80px 0"></div>
  <div class="abs" role="img" aria-label="Photo of a happy team joining hands over an office desk" style="left:592px;top:2308px;width:486px;height:354px;border-radius:60px 0 80px 0;background:linear-gradient(135deg,#c9c6c2,#8e8a86 55%,#4b4845)"></div>

  <!-- why choose -->
  <div class="abs" role="img" aria-label="Decorative dotted pattern" style="left:0;top:2995px;width:145px;height:195px;background:var(--orange-soft)"></div>
  <div class="abs" role="img" aria-label="Photo of smiling coworkers gathered around a laptop" style="left:79px;top:2770px;width:511px;height:385px;border-radius:60px 60px 80px 0;background:linear-gradient(135deg,#e9e6e3,#b8b3ae 55%,#6f6a66)"></div>
  <h2 class="h2" style="left:635px;top:2807px">WHY CHOOSE US</h2>
  <p class="para" style="left:635px;top:2872px;width:500px">Lorem ipsum dolor sit amet consectetur adipiscingi elit sed do eiusmod tempor incididunt ut labore</p>
  <div class="abs" style="left:635px;top:2955px;font-size:18px;font-weight:700;color:#333">ADVANTAGE</div>
  <ul class="abs" style="left:635px;top:2988px;list-style:none;font-size:18.5px;line-height:43px;color:var(--text)">
    <li><svg width="16" height="16" viewBox="0 0 16 16" style="vertical-align:-2px;margin-right:8px"><circle cx="8" cy="8" r="8" fill="var(--orange)"/><path d="M4.5 8.2l2.3 2.3 4.7-4.7" stroke="#fff" stroke-width="1.8" fill="none"/></svg>Lorem ipsum dolor sit amet incididunt ut</li>
    <li><svg width="16" height="16" viewBox="0 0 16 16" style="vertical-align:-2px;margin-right:8px"><circle cx="8" cy="8" r="8" fill="var(--orange)"/><path d="M4.5 8.2l2.3 2.3 4.7-4.7" stroke="#fff" stroke-width="1.8" fill="none"/></svg>Lorem ipsum dolor sit amet viverra sid</li>
    <li><svg width="16" height="16" viewBox="0 0 16 16" style="vertical-align:-2px;margin-right:8px"><circle cx="8" cy="8" r="8" fill="var(--orange)"/><path d="M4.5 8.2l2.3 2.3 4.7-4.7" stroke="#fff" stroke-width="1.8" fill="none"/></svg>Risus commodo viverra maecenas</li>
  </ul>

  <!-- contact -->
  <div class="abs" role="img" aria-label="Dark photograph of a team working together" style="left:0;top:3282px;width:1200px;height:578px;background:linear-gradient(90deg,#2a2a2a,#1b1b1b 50%,#252525)"></div>
  <h2 class="h2" style="left:0;width:1200px;top:3345px;text-align:center;color:var(--white)">CONTACT US</h2>
  <p class="para" style="left:0;width:1200px;top:3411px;text-align:center;color:var(--white)">Lorem ipsum dolor sit amet consectetur adipiscingi<br>elit sed do eiusmod tempor incididunt ut labore</p>
  <div class="field" style="left:245px;top:3522px;width:332px;height:50px">Enter Your Name</div>
  <div class="field" style="left:245px;top:3588px;width:332px;height:50px">Email Address</div>
  <div class="field" style="left:245px;top:3653px;width:332px;height:50px">Phone No</div>
  <div class="field" style="left:592px;top:3522px;width:363px;height:181px">Leave your message !</div>
  <div class="btn" style="left:499px;top:3732px;width:202px;height:50px;font-size:14px">Submit Now</div>

  <!-- footer -->
  <div class="fhead" style="left:79px">ABOUT US</div>
  <p class="abs" style="left:79px;top:3962px;font-size:17px;line-height:34px;color:var(--text);white-space:nowrap">Lorem ipsum dolor sit amet consecter<br>adipiscingi elit sed do eiusmod tempor<br>incididunt ut labore vsiverra idm tote</p>
  <div class="social" style="left:79px" aria-label="Social profile"></div>
  <div class="social" style="left:135px" aria-label="Social profile"></div>
  <div class="social" style="left:195px" aria-label="Social profile"></div>
  <p class="abs" style="left:79px;top:4145px;font-size:16px;color:var(--text)">Copyright © 2022 <span style="color:var(--orange)">Velquo.</span></p>

  <div class="fhead" style="left:478px">QUICK LINKS</div>
  <ul class="flist" style="left:478px"><li>Home</li><li>About Us</li><li>Our Features</li><li>Blog</li><li>Contact</li></ul>

  <div class="fhead" style="left:675px">OTHERS LINK</div>
  <ul class="flist" style="left:675px"><li>Terms &amp; Condition</li><li>Privacy Policy</li><li>Cookie</li><li>Resister Now</li><li>User Login</li></ul>

  <div class="fhead" style="left:890px">CONTACT INFO</div>
  <div class="cicon" style="top:3955px"><svg width="20" height="20" viewBox="0 0 24 24"><path fill="#fff" d="M6.6 10.8a15 15 0 0 0 6.6 6.6l2.2-2.2a1 1 0 0 1 1-.25 11.4 11.4 0 0 0 3.6.57 1 1 0 0 1 1 1V20a1 1 0 0 1-1 1A17 17 0 0 1 3 4a1 1 0 0 1 1-1h3.5a1 1 0 0 1 1 1c0 1.25.2 2.45.57 3.57a1 1 0 0 1-.25 1z"/></svg></div>
  <p class="abs" style="left:961px;top:3953px;font-size:17px;line-height:27px;color:var(--text)">Phone:<br>555-014-2290</p>
  <div class="cicon" style="top:4022px"><svg width="20" height="20" viewBox="0 0 24 24"><path fill="#fff" d="M3 9l9-6 9 6v11H3z"/><path d="M6 11l6 4 6-4" stroke="var(--orange)" stroke-width="2" fill="none"/></svg></div>
  <p class="abs" style="left:961px;top:4020px;font-size:17px;line-height:27px;color:var(--text)">Email:<br>contact@velquo.com</p>
  <p class="abs" style="left:890px;top:4118px;font-size:17px;font-weight:500;color:var(--ink);border-bottom:1.5px solid var(--ink)">Find Us on Map <svg width="16" height="12" viewBox="0 0 16 12" style="margin-left:4px"><path d="M1 6H14M9 1l5 5-5 5" stroke="var(--ink)" stroke-width="2" fill="none"/></svg></p>

</div>
</body>
</html>
```